Unique Beautiful Realtor business card

I need a unique business card that includes my logo, my firms logo, my picture and phone number. The colors should compliment my logo.

Target Market(s)

People who want to buy or sell a home in South Florida

Contact Information for Business Card

Use two sides and work with the DRM Coastal Homes logo as a theme.
The Harlow Benton should be small and discreet, it is a requirement to be there but should be small. My photo should be integrated artistically.

Font styles to use
Serif
Sans Serif

Colors

Designer to choose colors to be used in the design.

Requirements
Must have
• My logo, Harlow Benton logo, my photo, my phone number, (954-283-6091) and my website address. (www.drmcoastalhomes.example)
• Also my name, Dana R. Moreland, PA, Realtor
• Also “The Pet Friendly Realtor”

```html
<!DOCTYPE html>
<html lang="en">
<head>
<meta charset="utf-8">
<title>Dana R. Moreland – Business Card</title>
<link href="https://fonts.googleapis.com/css2?family=Prompt:wght@500;600&display=swap" rel="stylesheet">
<style>
  :root {
    --navy: #1b3f6d;
    --navy-deep: #13467a;
    --sky: #cde9f4;
    --olive: #9b9c43;
    --sun: #fcd247;
    --white: #ffffff;
    --photo-top: #9fb6a0;
    --photo-bottom: #6e7f86;
  }
  * { box-sizing: border-box; margin: 0; padding: 0; }
  html, body { width: 1008px; height: 1200px; overflow: hidden; background: var(--white); }
  body { position: relative; font-family: "Prompt", sans-serif; color: var(--navy); }

  .card-front {
    position: absolute; left: 13px; top: 31px; width: 982px; height: 549px;
    border: 3px solid var(--navy); background: var(--white); overflow: hidden;
  }
  .info-panel {
    position: absolute; left: 0; top: 0; width: 491px; height: 100%;
    background: var(--sky);
  }
  .tagline {
    position: absolute; left: 27px; top: 62px;
    font-size: 33px; font-weight: 600; color: var(--olive); white-space: nowrap;
  }
  .agent-name {
    position: absolute; left: 22px; top: 172px;
    font-size: 50px; font-weight: 600; color: var(--navy); white-space: nowrap;
  }
  .agent-title {
    position: absolute; left: 0; width: 491px; top: 240px; text-align: center;
    font-size: 31px; font-weight: 600; color: var(--navy);
  }
  .contact-line {
    position: absolute; left: 30px; display: flex; align-items: center; gap: 18px;
    font-size: 24px; font-weight: 500; color: var(--navy); white-space: nowrap;
  }
  .contact-line.phone { top: 336px; }
  .contact-line.web { top: 388px; }
  .contact-icon { width: 34px; height: 34px; flex: none; }

  .brokerage {
    position: absolute; left: 8px; bottom: 8px; display: flex; align-items: center; gap: 8px;
    font-size: 19px; font-weight: 500; color: var(--navy); white-space: nowrap;
  }
  .brokerage-mark { width: 14px; height: 14px; background: #8a1f46; }

  .photo-area { position: absolute; left: 0; top: 0; width: 982px; height: 549px; }

  .brand-name {
    position: absolute; left: 530px; top: 420px; width: 430px;
    display: flex; align-items: center; justify-content: center; gap: 14px;
    font-size: 33px; font-weight: 600; color: var(--navy); white-space: nowrap;
  }
  .brand-dot { width: 28px; height: 28px; border-radius: 50%; background: var(--sun); flex: none; }

  .card-back {
    position: absolute; left: 0; top: 607px; width: 1008px; height: 576px;
    background: var(--navy-deep);
  }
  .back-frame {
    position: absolute; left: 206px; top: 113px; width: 596px; height: 349px;
    background: var(--white); border: 9px solid var(--sun);
    display: flex; align-items: center; justify-content: center; gap: 18px;
    padding: 0 30px;
  }
  .back-frame .brand-dot { width: 42px; height: 42px; }
  .back-brand {
    font-size: 44px; font-weight: 600; color: var(--navy); white-space: nowrap;
  }
</style>
</head>
<body>
  <section class="card-front">
    <div class="info-panel">
      <p class="tagline">The Pet Friendly Realtor</p>
      <h1 class="agent-name">Dana R. Moreland</h1>
      <p class="agent-title">PA, Realtor</p>
      <p class="contact-line phone">
        <svg class="contact-icon" viewBox="0 0 34 34" aria-hidden="true">
          <circle cx="17" cy="17" r="17" fill="var(--navy)"/>
          <path d="M12 9c1-.6 2-.3 2.5.6l1.3 2.4c.4.8.2 1.6-.5 2.1l-1 .7c.8 2 2.2 3.5 4.1 4.5l.8-1c.6-.7 1.4-.8 2.1-.4l2.4 1.4c.8.5 1 1.5.5 2.4-.9 1.6-2.5 2.4-4.3 1.8C14.8 22.9 11 19 9.9 14.2 9.5 12 10.4 10 12 9z" fill="var(--white)"/>
        </svg>
        954-283-6091
      </p>
      <p class="contact-line web">
        <svg class="contact-icon" viewBox="0 0 34 34" aria-hidden="true">
          <circle cx="17" cy="17" r="17" fill="var(--navy)"/>
          <g fill="none" stroke="var(--white)" stroke-width="1.5">
            <circle cx="17" cy="17" r="8"/>
            <ellipse cx="17" cy="17" rx="3.5" ry="8"/>
            <line x1="9" y1="17" x2="25" y2="17"/>
            <line x1="10.5" y1="13" x2="23.5" y2="13"/>
            <line x1="10.5" y1="21" x2="23.5" y2="21"/>
          </g>
        </svg>
        www.drmcoastalhomes.example
      </p>
      <p class="brokerage"><span class="brokerage-mark"></span>Harlow Benton</p>
    </div>

    <svg class="photo-area" viewBox="0 0 982 549">
      <defs>
        <linearGradient id="photoTone" x1="0" y1="0" x2="0" y2="1">
          <stop offset="0" stop-color="var(--photo-top)"/>
          <stop offset="1" stop-color="var(--photo-bottom)"/>
        </linearGradient>
      </defs>
      <path d="M630 0 Q650 300 982 335 L982 0 Z" fill="url(#photoTone)" role="img" aria-label="Portrait photo of the realtor by a waterfront"/>
      <path d="M616 0 Q634 330 982 368 L982 335 Q650 300 630 0 Z" fill="var(--sun)"/>
    </svg>

    <p class="brand-name"><span class="brand-dot"></span>DRM Coastal Homes</p>
  </section>

  <section class="card-back">
    <div class="back-frame">
      <span class="brand-dot"></span>
      <p class="back-brand">DRM Coastal Homes</p>
    </div>
  </section>
</body>
</html>
```